Digital Marketing company needs business cards

We are a digital marketing company providing SEO, Bidlane and Web Development services in Australia and New Zealand. Colours and icons have to match the current website (kestrelworks.com.au). We'd like to keep the cards simple and clean, using the artwork we have as the background of the slider of the website (the triangles). The card should have horizontal layout.
If we could have our core services on the reverse side that'd be great:
SEO
BidLane
Web Design&Development
Target Market(s)
Medium size to large businesses
Industry/Entity Type
Digital

```html
<!DOCTYPE html>
<html lang="en">
<head>
<meta charset="utf-8">
<title>Kestrelworks business cards</title>
<link href="https://fonts.googleapis.com/css2?family=Open+Sans:wght@400;600;700&display=swap" rel="stylesheet">
<style>
  :root {
    --brand-blue: #0a88bb;
    --stripe-grey: #5f6063;
    --ink: #2b2b2b;
    --muted: #555;
    --card-white: #ffffff;
    --backdrop: #e9e7e3;
  }
  * { box-sizing: border-box; margin: 0; padding: 0; }
  html, body { width: 1200px; height: 1019px; overflow: hidden; }
  body {
    background: var(--backdrop);
    font-family: "Open Sans", Arial, sans-serif;
    display: flex;
    flex-direction: column;
    align-items: center;
    justify-content: center;
    gap: 56px;
  }
  .card {
    position: relative;
    width: 760px;
    height: 434px;
    background: var(--card-white);
    box-shadow: 0 10px 28px rgba(0,0,0,.18);
    overflow: hidden;
  }
  .card-art { position: absolute; inset: 0; width: 100%; height: 100%; }
  .brand {
    position: absolute;
    left: 50px;
    top: 168px;
    display: flex;
    align-items: center;
    gap: 14px;
  }
  .brand-name {
    font-size: 42px;
    font-weight: 600;
    color: var(--brand-blue);
    letter-spacing: -1px;
  }
  .brand-dot {
    width: 38px; height: 38px;
    border-radius: 50%;
    background: var(--brand-blue);
  }
  .contact {
    position: absolute;
    left: 420px;
    top: 36px;
    color: var(--ink);
  }
  .person-name { font-size: 22px; font-weight: 700; color: var(--brand-blue); line-height: 1.3; }
  .person-role { font-size: 14px; color: var(--muted); margin-bottom: 20px; }
  .address { font-size: 14px; font-weight: 700; line-height: 1.35; margin-bottom: 12px; }
  .contact-list { list-style: none; font-size: 13px; color: var(--muted); }
  .contact-list li { display: flex; align-items: center; gap: 10px; height: 22px; white-space: nowrap; }
  .contact-list svg { width: 14px; height: 14px; fill: var(--brand-blue); flex: none; }
  .card-back { background: var(--brand-blue); }
  .back-panel {
    position: absolute;
    left: 430px;
    top: 0;
    width: 220px;
    height: 434px;
    background: var(--card-white);
  }
</style>
</head>
<body>

<section class="card card-front">
  <svg class="card-art" viewBox="0 0 760 434" aria-hidden="true">
    <path d="M0 372 C420 400 700 320 760 120" fill="none" stroke="var(--stripe-grey)" stroke-width="9"/>
    <path d="M0 388 C430 416 710 336 760 142 L760 434 L0 434 Z" fill="var(--brand-blue)"/>
  </svg>

  <div class="brand">
    <span class="brand-name">kestrelworks</span>
    <span class="brand-dot"></span>
  </div>

  <div class="contact">
    <p class="person-name">Daniel Hartley</p>
    <p class="person-role">President &amp; CEO</p>
    <p class="address">Level 4, 12 Harbour Lane<br>Road NSW</p>
    <ul class="contact-list">
      <li><svg viewBox="0 0 24 24"><path d="M6.6 10.8a15 15 0 0 0 6.6 6.6l2.2-2.2a1 1 0 0 1 1-.25 11 11 0 0 0 3.6.6 1 1 0 0 1 1 1V20a1 1 0 0 1-1 1A17 17 0 0 1 3 4a1 1 0 0 1 1-1h3.5a1 1 0 0 1 1 1 11 11 0 0 0 .6 3.6 1 1 0 0 1-.25 1z"/></svg>(012) 555 0142</li>
      <li><svg viewBox="0 0 24 24"><path d="M7 1h10a2 2 0 0 1 2 2v18a2 2 0 0 1-2 2H7a2 2 0 0 1-2-2V3a2 2 0 0 1 2-2zm0 3v14h10V4z"/></svg>(012) 555 0143</li>
      <li><svg viewBox="0 0 24 24"><path d="M6 2h9l3 3v5H6zM4 11h16a2 2 0 0 1 2 2v8H2v-8a2 2 0 0 1 2-2zm3 4v2h10v-2z"/></svg>(012) 555 0144</li>
      <li><svg viewBox="0 0 24 24"><path d="M2 5h20v14H2zm2 2v.5l8 5 8-5V7l-8 5z"/></svg>hello@kestrelworks.com.au</li>
    </ul>
  </div>
</section>

<section class="card card-back">
  <div class="back-panel"></div>
</section>

</body>
</html>
```